Webshop for furniture and lamps

We need a design for a web shop with APP that should have two options:
1-Webshop in general which should attract to private customer in general and
2-Website that is meant to attract big customers as hotels and restaurants who would have their own customerize login.

That's the idea behind the shop.

It should be diveded into 4 parts
vintage furniture
rattan set outdoor and indoor
lamps and
wooden wall decor

The name of the shop is borgo veneria!

Please kindly make me an offer.

Reason: Dear designers, so far there hasn't been a design that really matched. Look up German web sites like www.trevolind.de or www.quandor17.de... Haven't been convinced by designs! Sorry folks. Please submit some new ones. Kind regards Tam

```html
<!DOCTYPE html>
<html lang="en">
<head>
<meta charset="utf-8">
<title>Borgo Veneria – Furniture &amp; Lamps</title>
<link href="https://fonts.googleapis.com/css2?family=Oswald:wght@400;500;600&family=Arimo:wght@400;700&display=swap" rel="stylesheet">
<style>
:root{
  --page:#ececec;
  --frame:#8f8f8f;
  --header:#2a2722;
  --header-stripe:#34302a;
  --ink:#1a1a1a;
  --white:#ffffff;
  --logo:#f2a33a;
  --accent:#f39a2d;
  --link:#2aa7e0;
  --nav-top:#8a8a8a;
  --nav-bottom:#5a5a5a;
  --tile:#e9e9e9;
  --tile-text:#3a3a3a;
  --muted:#8a8a8a;
  --btn:#8d8356;
  --red:#c8262c;
  --social:#4a4a4a;
  --social-mark:#e6e6e6;
}
*{box-sizing:border-box;margin:0;padding:0}
html,body{width:1067px;height:1200px;overflow:hidden;background:var(--white)}
body{font-family:"Arimo",Arial,sans-serif;color:var(--ink)}
.page{position:absolute;left:4px;top:4px;width:1059px;height:1192px;background:var(--page);border:8px solid var(--frame);border-radius:3px;overflow:hidden}
.abs{position:absolute}
.header-band{left:0;top:0;width:1043px;height:388px;background:repeating-linear-gradient(90deg,var(--header) 0 3px,var(--header-stripe) 3px 5px)}
.logo-name{left:70px;top:20px;font-family:"Oswald",sans-serif;font-weight:400;font-size:36px;line-height:40px;color:var(--logo);letter-spacing:2px;text-transform:uppercase}
.account{left:784px;top:26px;color:var(--white);font-size:15px;line-height:20px}
.account p:nth-child(2){padding-left:6px}
.nav{left:51px;top:105px;width:926px;height:34px;border-radius:3px;background:linear-gradient(var(--nav-top),var(--nav-bottom))}
.nav a{font-family:"Oswald",sans-serif;font-weight:500;font-size:18px;color:var(--white);text-decoration:none;position:absolute;top:4px}
.search{position:absolute;left:623px;top:5px;width:277px;height:25px;background:#2e2e2e;border-radius:2px;color:#9a9a9a;font-style:italic;font-family:Georgia,serif;font-size:16px;padding:2px 0 0 60px}
.search svg{position:absolute;right:12px;top:5px}
.style-tab{left:0;top:61px;width:35px;height:236px;background:var(--white);border-radius:0 6px 6px 0;display:flex;flex-direction:column;align-items:center;padding-top:10px}
.style-tab span{writing-mode:vertical-rl;transform:rotate(180deg);font-size:19px;color:var(--ink)}
.style-tab b{font-size:20px;margin-bottom:10px}
.social{left:994px;width:44px;height:54px;background:var(--social);display:flex;align-items:center;justify-content:center;box-shadow:0 1px 2px rgba(0,0,0,.4)}
.social i{display:block;width:20px;height:20px;border-radius:50%;background:var(--social-mark)}
.hero{left:53px;top:145px;width:924px;height:426px;background:var(--white);box-shadow:0 2px 4px rgba(0,0,0,.35)}
.slide{left:11px;top:10px;width:565px;height:406px;background:linear-gradient(180deg,#7b7c5c 0%,#a19478 30%,#6f6a5e 60%,#3f3c39 100%)}
.caption{left:0;top:303px;width:429px;height:95px;background:rgba(30,30,30,.82);padding:6px 10px;color:var(--white)}
.caption h2{font-family:"Oswald",sans-serif;font-weight:600;font-size:25px;line-height:30px}
.caption h2 em{font-style:normal;color:var(--accent)}
.caption p{font-size:12.5px;line-height:17px;margin-top:2px}
.caption a{font-family:"Oswald",sans-serif;font-size:13px;font-weight:600;color:var(--link);text-decoration:none}
.arrows{left:3px;top:275px;display:flex;gap:2px}
.arrows i{display:block;width:28px;height:31px;background:#222}
.arrows i+i{background:var(--red)}
.tile{left:598px;width:326px;height:96px;background:var(--tile);overflow:hidden}
.tile h3{position:absolute;font-family:"Oswald",sans-serif;font-weight:500;font-size:24px;color:var(--tile-text);line-height:28px;white-space:nowrap}
.tile small{position:absolute;font-family:"Oswald",sans-serif;font-size:12px;color:#666}
.tile .pic{position:absolute;top:0;height:96px}
.box{background:var(--white);box-shadow:0 2px 4px rgba(0,0,0,.35)}
.box-head{height:32px;background:var(--ink);color:var(--white);font-family:"Oswald",sans-serif;font-weight:500;font-size:18px;line-height:32px;padding-left:14px;position:relative}
.categories{left:51px;top:635px;width:229px;height:424px}
.categories ul{list-style:disc;padding:20px 0 0 44px;color:var(--muted);font-size:15.5px;line-height:19.6px}
.products{left:320px;top:635px;width:657px;height:424px}
.products .box-head span{position:absolute;top:0}
.card{width:258px;height:298px;border:1px solid #d8d8d8;background:var(--white);text-align:center}
.card .pic{height:198px;border-bottom:1px solid #d8d8d8}
.card h4{font-weight:400;font-size:16px;margin-top:6px;color:#333}
.card .price{font-family:Georgia,serif;font-size:16px;margin-top:2px}
.card .cart{display:inline-block;margin-top:5px;background:var(--btn);color:var(--white);font-family:"Oswald",sans-serif;font-size:13px;padding:2px 9px}
.card .links{font-size:12px;margin-top:6px;color:#333}
.helpline{left:783px;top:1039px;width:194px;height:62px;background:var(--ink);border-radius:9px 9px 0 0;color:var(--white);font-family:"Oswald",sans-serif;font-weight:600;font-size:28px;text-align:center;padding-top:16px}
.footer{left:0;top:1099px;width:1043px;height:81px;background:var(--ink);color:var(--white)}
.privacy{left:39px;top:6px;width:600px;font-size:9.5px;line-height:12px;text-decoration:underline}
.rights{left:50px;top:50px;font-size:13px}
.footer-nav{left:532px;top:50px;font-size:13px;word-spacing:2px}
.footer-mark{left:988px;top:49px;width:18px;height:18px;border-radius:50%;background:var(--link)}
</style>
</head>
<body>
<div class="page">
  <div class="abs header-band"></div>

  <div class="abs logo-name">Borgo<br>Veneria</div>

  <div class="abs account">
    <p>Welcome to our shop</p>
    <p>Login &nbsp;|&nbsp; Signup</p>
    <p>(0) Cart Successful &nbsp;0.00</p>
  </div>

  <nav class="abs nav">
    <a style="left:13px">Home</a>
    <a style="left:109px">About</a>
    <a style="left:203px">Categories</a>
    <a style="left:331px">Shop</a>
    <a style="left:415px">Join Us?</a>
    <a style="left:520px">Contacts</a>
    <div class="search">Search Entire Store
      <svg width="16" height="16" viewBox="0 0 16 16"><circle cx="6.5" cy="6.5" r="4.5" fill="none" stroke="#ddd" stroke-width="2"/><line x1="10" y1="10" x2="14.5" y2="14.5" stroke="#ddd" stroke-width="2.5"/></svg>
    </div>
  </nav>

  <div class="abs style-tab"><b>+</b><span>Classic Style</span></div>

  <a class="abs social" style="top:115px" aria-label="Kinly"><i></i></a>
  <a class="abs social" style="top:174px" aria-label="Chirpo"><i></i></a>
  <a class="abs social" style="top:233px" aria-label="Plusly"><i></i></a>
  <a class="abs social" style="top:294px" aria-label="Pinora"><i></i></a>

  <section class="abs hero">
    <div class="abs slide" role="img" aria-label="Black rattan dining set with glass table on a wooden deck">
      <div class="abs arrows">
        <i><svg width="28" height="31" viewBox="0 0 28 31"><path d="M17 8 L10 15.5 L17 23" fill="none" stroke="#fff" stroke-width="3"/></svg></i>
        <i><svg width="28" height="31" viewBox="0 0 28 31"><path d="M11 8 L18 15.5 L11 23" fill="none" stroke="#fff" stroke-width="3"/></svg></i>
      </div>
      <div class="abs caption">
        <h2><em>HOTEL</em> FURNITURE</h2>
        <p>Lorem ipsum dolor sit amet, consectetur adipisicing elit, sed do eiusmod tempor incididunt ut labore et dolore magna aliqua.</p>
        <a>READ MORE</a>
      </div>
    </div>

    <div class="abs tile" style="top:8px">
      <div class="pic" role="img" aria-label="Rattan chair set around a round table" style="left:196px;width:130px;background:linear-gradient(135deg,#efe9e2,#b9784d)"></div>
      <h3 style="left:6px;top:14px">Vintage Furniture</h3>
      <small style="left:15px;top:48px">Shop Now</small>
    </div>
    <div class="abs tile" style="top:112px">
      <div class="pic" role="img" aria-label="Brass floor lamp with cream shade" style="left:0;width:190px;background:linear-gradient(180deg,#f0e3c6,#ddd3bd 50%,#e9e9e9)"></div>
      <h3 style="left:196px;top:20px">Rattan Set</h3>
      <small style="left:201px;top:52px">Shop Now</small>
    </div>
    <div class="abs tile" style="top:216px">
      <h3 style="left:6px;top:18px">Lamps</h3>
      <small style="left:11px;top:52px">Shop Now</small>
      <div class="pic" role="img" aria-label="Round grey rattan table with tucked seats" style="left:120px;width:206px;background:linear-gradient(135deg,#8a8a8a,#4e4e4e)"></div>
    </div>
    <div class="abs tile" style="top:320px">
      <div class="pic" role="img" aria-label="Wooden block wall panel" style="left:0;width:100px;background:linear-gradient(135deg,#9b6a45,#5e3b22)"></div>
      <h3 style="left:111px;top:16px">Wooden Wall Decor</h3>
      <small style="left:117px;top:54px">Shop Now</small>
    </div>
  </section>

  <aside class="abs box categories">
    <div class="box-head">SHOP CATEGORIES</div>
    <ul>
      <li>Vintage Furniture</li>
      <li>Rattan Set</li>
      <li>Lamps</li>
      <li>Wooden Wall Décor</li>
      <li>Another category</li>
      <li>Another Category</li>
      <li>Second Final</li>
      <li>Many More Categories</li>
    </ul>
  </aside>

  <section class="abs box products">
    <div class="box-head"><span style="left:15px">Product List</span><span style="left:326px">Order By</span><span style="left:539px">Date:</span></div>
    <div class="abs card" style="left:41px;top:80px">
      <div class="pic" role="img" aria-label="Outdoor rattan lounge set in a garden" style="background:linear-gradient(180deg,#dfe8ee 0%,#6f8a4e 45%,#8a7a5e 75%,#6e6353 100%)"></div>
      <h4>Product Name</h4>
      <p class="price">£ 120.00</p>
      <span class="cart">ADD TO CART</span>
      <p class="links">Add to wish list &nbsp;&nbsp;|&nbsp;&nbsp; Add to compare</p>
    </div>
    <div class="abs card" style="left:333px;top:80px">
      <div class="pic" role="img" aria-label="Round grey rattan table with stools" style="background:linear-gradient(160deg,#ffffff 0%,#7a7a7a 40%,#4a4a4a 70%,#ffffff 100%)"></div>
      <h4>Product Name</h4>
      <p class="price">£ 120.00</p>
      <span class="cart">ADD TO CART</span>
      <p class="links">Add to wish list &nbsp;&nbsp;|&nbsp;&nbsp; Add to compare</p>
    </div>
  </section>

  <div class="abs helpline">HELP LINE</div>

  <footer class="abs footer">
    <p class="abs privacy">Privacy Policy Statement will be written here to be seen by visitors of this site. Privacy Policy Statement will be written here to be seen by visitors of this site. Privacy Policy Statement will be written here to be seen by visitors of this site.</p>
    <p class="abs rights">All Rights Reserved. &nbsp;&nbsp;&nbsp;© BORGO VENERIA</p>
    <p class="abs footer-nav">Home &nbsp;&nbsp;| &nbsp;About Us &nbsp;&nbsp;| &nbsp;Contacts &nbsp;&nbsp;| &nbsp;Categories &nbsp;&nbsp;@borgo_veneria</p>
    <a class="abs footer-mark" aria-label="Chirpo"></a>
  </footer>
</div>
</body>
</html>
```